Bramblefield Circle for Nurses - New facebook banner design + logo

We are setting up a new private facebook group called Bramblefield Circle for Nurses. Administered by Marla Teske, Marla helps women in healthcare to crush their life and health goals so they can bring their best version of themselves to others. We would like a modern / contemporary header design incorporating colours / fonts from the attached moodboard. An icon or image representing a woman. Our initial thinking included an icon of a woman outline? Just thoughts. Bright bold colours incorporating some gold / marble. See existing business brandboard however elements of Bramblefield Circle for Nurses DO NOT need to be aligned to this brandboard. Images should represent personal strength (not physical strength ie. fitness), community and femininity.

Target Market(s)

Women in healthcare

Industry/Entity Type

Healthcare

Font styles to use
Sans Serif

Requirements
Must have
• unique iconology that can be used to represent the group. I've attached some examples of woman silhouettes. Doesn't need to be full body but iconology may just include head / shoulders / torso.

```html
<!DOCTYPE html>
<html lang="en">
<head>
<meta charset="utf-8">
<title>Bramblefield Circle for Nurses – Group Banner</title>
<link rel="stylesheet" href="https://fonts.googleapis.com/css2?family=Poppins:wght@600&family=Questrial&display=swap">
<style>
  :root {
    --page-bg: #1c1c1c;
    --banner-bg: #ffffff;
    --ink: #111111;
    --text-grey: #333333;
    --accent-orange: #ef8f4a;
    --wash-pink: #f6c9d0;
    --wash-blue: #a9d8f2;
    --leaf-green: #7fb27a;
    --leaf-light: #c9df8c;
  }
  * { margin: 0; padding: 0; box-sizing: border-box; }
  html, body {
    width: 1200px;
    height: 848px;
    overflow: hidden;
    background: var(--page-bg);
  }
  .banner {
    position: absolute;
    left: 0;
    top: 110px;
    width: 1200px;
    height: 628px;
    background: var(--banner-bg);
    overflow: hidden;
  }
  .wash {
    position: absolute;
    filter: blur(18px);
  }
  .wash--pink {
    left: -40px; top: -30px;
    width: 420px; height: 560px;
    background: radial-gradient(ellipse at 45% 35%, var(--wash-pink) 0%, rgba(246,201,208,0.6) 50%, rgba(246,201,208,0) 75%);
  }
  .wash--blue {
    right: -40px; top: 120px;
    width: 440px; height: 560px;
    background: radial-gradient(ellipse at 60% 60%, var(--wash-blue) 0%, rgba(169,216,242,0.6) 50%, rgba(169,216,242,0) 75%);
  }
  .foliage {
    position: absolute;
    border-radius: 40%;
    opacity: 0.75;
  }
  .foliage--top-left {
    left: -30px; top: -30px; width: 170px; height: 300px;
    background: radial-gradient(ellipse at 20% 20%, var(--leaf-green) 0%, rgba(201,223,140,0.5) 45%, rgba(255,255,255,0) 72%);
  }
  .foliage--bottom-left {
    left: -30px; bottom: -40px; width: 170px; height: 250px;
    background: radial-gradient(ellipse at 25% 80%, var(--leaf-green) 0%, rgba(201,223,140,0.5) 45%, rgba(255,255,255,0) 72%);
  }
  .foliage--top-right {
    right: -30px; top: -30px; width: 180px; height: 270px;
    background: radial-gradient(ellipse at 75% 20%, var(--leaf-light) 0%, rgba(127,178,122,0.45) 45%, rgba(255,255,255,0) 72%);
  }
  .foliage--bottom-right {
    right: -30px; bottom: -40px; width: 170px; height: 290px;
    background: radial-gradient(ellipse at 75% 80%, var(--leaf-green) 0%, rgba(201,223,140,0.5) 45%, rgba(255,255,255,0) 72%);
  }
  .group-name {
    position: absolute;
    left: 0; right: 0;
    top: 150px;
    text-align: center;
    font-family: "Questrial", sans-serif;
    color: var(--ink);
    font-size: 62px;
    line-height: 1.12;
  }
  .group-name__dot {
    display: block;
    width: 46px; height: 46px;
    margin: 0 auto 22px;
    border-radius: 50%;
    background: var(--accent-orange);
  }
  .admin-line {
    position: absolute;
    left: 0; right: 0;
    top: 456px;
    text-align: center;
    font-family: "Questrial", sans-serif;
    font-size: 32px;
    color: var(--text-grey);
  }
  .name-accent {
    font-family: "Poppins", sans-serif;
    font-weight: 600;
    color: var(--accent-orange);
  }
  .admin-line .name-accent {
    text-transform: uppercase;
    letter-spacing: 1px;
    font-size: 29px;
  }
  .mission {
    position: absolute;
    left: 0; right: 0;
    top: 527px;
    text-align: center;
    font-family: "Questrial", sans-serif;
    font-size: 22px;
    line-height: 30px;
    letter-spacing: 0.3px;
    color: var(--text-grey);
  }
</style>
</head>
<body>
  <main class="banner">
    <div class="wash wash--pink" role="img" aria-label="Soft pink watercolour wash"></div>
    <div class="wash wash--blue" role="img" aria-label="Soft blue watercolour wash"></div>
    <div class="foliage foliage--top-left" role="img" aria-label="Watercolour leafy branches"></div>
    <div class="foliage foliage--bottom-left" role="img" aria-label="Watercolour leafy branches"></div>
    <div class="foliage foliage--top-right" role="img" aria-label="Watercolour leafy branches"></div>
    <div class="foliage foliage--bottom-right" role="img" aria-label="Watercolour leafy branches"></div>

    <h1 class="group-name">
      <span class="group-name__dot"></span>
      Bramblefield Circle<br>for Nurses
    </h1>

    <p class="admin-line">Administered by <span class="name-accent">Marla Teske</span></p>

    <p class="mission">
      <span class="name-accent">Marla</span> helps women in healthcare to crush their life and health goals so<br>
      they can bring their best version of themselves to others.
    </p>
  </main>
</body>
</html>
```